Company Brochure - Recruitment Agency

We need a company brochure. We are a recruitment firm and we want to depict a professional, energetic and result oriented image. We would like our brochure to be in line with our logo design. A color filled and modern design will be a big plus.

We want the brochure to be smaller than a A4 size paper, elongated in shape with 3 pages on each side (see attached pics)
Updates

Reason: Need more designs to compare. Did not like the ones I received so far.

Target Market(s)

Big Corporations and Global Multinational companies

Industry/Entity Type

It Company

Requirements
Must have
• 6 long-sided Pages Design (with 3 Pages on each side)
• Page Measurement: 26cm x 14cm (for each page)
• Brochure Measurement: 26cm x 14 cm (when folded)
Nice to have
• Theme in line with our logo design.
• Project a fast, energetic and professional image.
Should not have
• Am open at this moment

```html
<!DOCTYPE html>
<html lang="en">
<head>
<meta charset="utf-8">
<title>SwiftStaff Partners – Brochure</title>
<link href="https://fonts.googleapis.com/css2?family=Open+Sans:wght@400;600;700&family=Open+Sans+Condensed:wght@300;700&display=swap" rel="stylesheet">
<style>
:root{
  --green:#7cb82f;
  --green-dark:#4f8d1f;
  --green-pale:#e9f3dc;
  --ink:#3a3a3a;
  --muted:#6b6b6b;
  --paper:#ffffff;
  --bg:#f3f3f3;
}
*{box-sizing:border-box;margin:0;padding:0}
html,body{width:771px;height:1200px;overflow:hidden;background:var(--bg);font-family:"Open Sans",Arial,sans-serif;color:var(--ink)}
.spread{position:absolute;left:25px;width:721px;background:var(--paper);box-shadow:0 2px 8px rgba(0,0,0,.18);overflow:hidden}
.spread.outside{top:25px;height:505px}
.spread.inside{top:580px;height:555px}
.panel{position:absolute;top:0;bottom:0;width:240px;padding:18px 16px}
.p1{left:0}.p2{left:240px;border-left:1px dashed #ddd}.p3{left:481px;border-left:1px dashed #ddd}
h2{font-size:14px;color:var(--green-dark);font-weight:700;margin-bottom:8px}
p{font-size:7.5px;line-height:1.55;color:var(--muted);margin-bottom:7px}
ol{list-style:none;font-size:7.5px;line-height:1.5;color:var(--muted)}
ol li{margin-bottom:7px;padding-left:14px;position:relative}
ol li span{position:absolute;left:0;color:var(--green-dark);font-weight:700}
.swoosh{position:absolute;left:0;bottom:0;width:721px;height:200px}
.contact{font-size:8px;line-height:1.8;color:var(--ink);margin-top:4px}
.contact div{display:flex;align-items:center;gap:6px;white-space:nowrap}
.dot{width:8px;height:8px;border-radius:50%;background:var(--green);flex:none}
.tagline{margin-top:30px;font-size:8px;line-height:1.6;color:var(--green-dark);text-align:center}
.brand{display:flex;align-items:center;gap:6px;font-weight:700;color:var(--green-dark);font-size:20px;letter-spacing:.3px;white-space:nowrap}
.brand .sq{width:12px;height:12px;background:var(--green);flex:none}
.brand-box{position:absolute;left:20px;bottom:70px;width:200px;height:60px;background:#fff;border:1px solid #cfe3b4;display:flex;align-items:center;justify-content:center}
.brand-box .brand{font-size:15px}
.cover-head{font-family:"Open Sans Condensed","Open Sans",sans-serif;font-weight:700;font-size:14px;line-height:1.2;color:var(--green-dark);text-align:right;white-space:nowrap}
.photo{position:absolute;background:linear-gradient(160deg,#d9dde2,#8c939b)}
.cover-photo{left:20px;top:84px;width:200px;height:200px;border-radius:4px}
.cover-brand{position:absolute;left:24px;top:310px}
.cover-brand .brand{font-size:18px}
.web{position:absolute;right:18px;bottom:14px;font-size:8px;color:#fff;font-weight:600;letter-spacing:.5px}
.services{list-style:none;font-size:8px;color:var(--ink);line-height:1.8}
.services li::before{content:"";display:inline-block;width:6px;height:6px;background:var(--green);margin-right:6px}
.boxes{display:grid;grid-template-columns:1fr 1fr;gap:8px;margin-top:6px}
.box{border:1px solid #cfe3b4;font-size:7px;color:var(--muted);line-height:1.55}
.box h3{background:var(--green);color:#fff;font-size:7.5px;font-weight:700;padding:3px 6px}
.box ul{list-style:none;padding:4px 6px}
.industry{left:240px;width:300px;border-left:1px dashed #ddd}
.side{left:540px;width:181px;border-left:none;padding-top:0}
.side-photo{position:relative;height:200px;margin:0 -16px 14px;background:linear-gradient(160deg,#e3e6ea,#7e868f)}
.footer-band{position:absolute;left:0;right:0;bottom:0;height:16px;background:var(--green)}
</style>
</head>
<body>

<section class="spread outside">
  <svg class="swoosh" viewBox="0 0 721 200" preserveAspectRatio="none" aria-hidden="true">
    <path d="M0 150 C200 90 420 200 721 90 L721 200 L0 200Z" fill="var(--green)"/>
    <path d="M0 170 C220 120 430 210 721 125 L721 200 L0 200Z" fill="var(--green-dark)"/>
  </svg>

  <div class="panel p1">
    <h2>Our Recruitment Process</h2>
    <p>We follow a clear, proven method to connect strong talent with leading employers.</p>
    <ol>
      <li><span>1.</span>Brief: we meet your team to learn the role, culture and goals.</li>
      <li><span>2.</span>Search: we tap our network and databases to find suitable candidates.</li>
      <li><span>3.</span>Screen: each profile is interviewed and assessed against your needs.</li>
      <li><span>4.</span>Present: you receive a focused shortlist with clear notes.</li>
      <li><span>5.</span>Support: we guide offers, onboarding and follow up after placement.</li>
    </ol>
  </div>

  <div class="panel p2">
    <div class="contact">
      <div><span class="dot"></span>Level 4, 18 Harbour Point Road, Singapore 048621</div>
      <div><span class="dot"></span>+65 6123 4567</div>
      <div><span class="dot"></span>+65 6123 4568</div>
      <div><span class="dot"></span>hello@swiftstaff-partners.com</div>
      <div><span class="dot"></span>www.swiftstaff-partners.com</div>
    </div>
    <p class="tagline">SwiftStaff Partners is an independent provider of HR solutions in Asia. We connect skilled people with growing firms across the region.</p>
    <div class="brand-box"><div class="brand"><span class="sq"></span>SwiftStaff Partners</div></div>
  </div>

  <div class="panel p3">
    <div class="cover-head">We understand<br>that the only thing consistent in<br>the business world is change</div>
    <div class="photo cover-photo" role="img" aria-label="Photo of a group of smiling business professionals"></div>
    <div class="cover-brand"><div class="brand"><span class="sq"></span>SwiftStaff Partners</div></div>
    <div class="web">www.swiftstaff-partners.com</div>
  </div>
</section>

<section class="spread inside">
  <div class="panel p1">
    <h2>Our Company</h2>
    <p>SwiftStaff Partners is an independent provider of HR solutions for leading firms and global groups.</p>
    <p>Our team brings deep sector knowledge and a wide network of skilled professionals ready to deliver.</p>
    <p>We focus on long-term partnerships, quality placements and fast, reliable service for every client.</p>
    <h2 style="margin-top:14px">Services</h2>
    <ul class="services">
      <li>Executive Search</li>
      <li>Contract Staffing</li>
      <li>Permanent Hiring</li>
      <li>HR Consulting</li>
      <li>Payroll Services</li>
    </ul>
  </div>

  <div class="panel industry">
    <h2>Industry Coverage</h2>
    <p>We place talent across a wide range of sectors, from technology to finance and energy.</p>
    <div class="boxes">
      <div class="box"><h3>Information Technology</h3><ul><li>Software Developers</li><li>Network Engineers</li><li>Project Managers</li><li>Data Analysts</li><li>Support</li></ul></div>
      <div class="box"><h3>Banking &amp; Finance</h3><ul><li>Accountants</li><li>Risk Analysts</li><li>Relationship Managers</li><li>Auditors</li><li>Treasury</li></ul></div>
      <div class="box"><h3>Engineering</h3><ul><li>Civil Engineers</li><li>Mechanical</li><li>Electrical</li><li>Site Supervisors</li><li>Planners</li></ul></div>
      <div class="box"><h3>Healthcare</h3><ul><li>Nurses</li><li>Pharmacists</li><li>Lab Staff</li><li>Clinic Managers</li><li>Therapists</li></ul></div>
      <div class="box"><h3>Telecom</h3><ul><li>RF Engineers</li><li>Field Technicians</li><li>Sales</li><li>Network Planning</li><li>Support</li></ul></div>
      <div class="box"><h3>Retail</h3><ul><li>Store Managers</li><li>Merchandisers</li><li>Buyers</li><li>Logistics</li><li>Customer Service</li></ul></div>
    </div>
  </div>

  <div class="panel side">
    <div class="side-photo" role="img" aria-label="Photo of business people standing together"></div>
    <div class="box" style="margin-bottom:10px"><h3>Key Functions</h3><ul><li>Sales &amp; Marketing</li><li>Human Resources</li><li>Operations</li><li>Legal</li><li>Administration</li></ul></div>
    <div class="box"><h3>Why Choose Us</h3><ul><li>Fast turnaround times</li><li>Deep candidate pool</li><li>Dedicated account managers</li><li>Clear, honest reporting</li></ul></div>
  </div>
  <div class="footer-band"></div>
</section>

</body>
</html>
```